Marrowby's Vacation Rentals Business Card

Multi Million dollar villa rentals in the Dominican Republic.

Industry/Entity Type

Business

Contact Information for Business Card

I am looking for a high-end look around my company name/logo (see attached) on one side incorporating the following info: first and last name, title, address, phone #, email and company website. On the backside I want to add a full color picture of one of our villas (see attached).

```html
<!DOCTYPE html>
<html lang="en">
<head>
<meta charset="utf-8">
<title>Marrowby's Vacation Rentals – Business Card</title>
<link rel="stylesheet" href="https://fonts.googleapis.com/css2?family=Libre+Baskerville:wght@400;700&family=Open+Sans:wght@400;600&display=swap">
<style>
  :root {
    --bg: #e9e6e1;
    --card-white: #ffffff;
    --card-black: #1f1f20;
    --accent: #f07a22;
    --text-light: #f2f2f2;
    --text-dark: #2a2a2a;
    --sky: #6fb2e6;
    --wall: #f1efe9;
    --pool: #2a8fd0;
  }
  * { margin: 0; padding: 0; box-sizing: border-box; }
  html, body { width: 1200px; height: 950px; overflow: hidden; }
  body {
    background: var(--bg);
    font-family: "Open Sans", sans-serif;
    position: relative;
  }
  .card {
    position: absolute;
    left: 250px;
    width: 700px;
    height: 400px;
    border-radius: 22px;
    overflow: hidden;
    box-shadow: 0 10px 30px rgba(0,0,0,0.22);
  }
  .card-front { top: 45px; background: var(--card-white); }
  .card-back { top: 505px; }
  .front-shape { position: absolute; inset: 0; width: 700px; height: 400px; }
  .brand {
    position: absolute;
    left: 80px;
    top: 62px;
    display: flex;
    align-items: center;
    gap: 16px;
  }
  .brand-dot {
    width: 48px; height: 48px; border-radius: 50%;
    background: var(--accent);
    flex: none;
  }
  .brand-name {
    font-family: "Libre Baskerville", serif;
    font-weight: 400;
    font-size: 30px;
    color: var(--text-dark);
    line-height: 1.2;
  }
  .brand-name .line { display: block; white-space: nowrap; }
  .contact {
    position: absolute;
    left: 60px;
    right: 40px;
    bottom: 42px;
    color: var(--text-light);
    font-size: 16px;
  }
  .contact-head {
    display: flex;
    align-items: baseline;
    gap: 12px;
    margin-bottom: 14px;
  }
  .person-name {
    font-family: "Libre Baskerville", serif;
    color: var(--accent);
    font-size: 26px;
  }
  .person-title { font-size: 16px; }
  .divider { color: #9a9a9a; }
  .contact-row {
    display: flex;
    align-items: center;
    gap: 8px;
    margin-bottom: 8px;
    white-space: nowrap;
  }
  .icon { width: 16px; height: 16px; flex: none; }
  .contact-row .gap { width: 14px; }
  .villa-photo {
    position: absolute; inset: 0;
    background: linear-gradient(100deg, var(--pool) 0%, #4aa6dc 22%, var(--wall) 40%, #e7e2d8 62%, #c9a07e 78%, var(--sky) 100%);
  }
  .back-brand {
    position: absolute;
    left: 24px;
    bottom: 24px;
    display: flex;
    align-items: center;
    gap: 8px;
    background: rgba(255,255,255,0.92);
    padding: 8px 14px;
    border-radius: 6px;
  }
  .back-brand .brand-dot { width: 18px; height: 18px; }
  .back-brand .brand-name { font-size: 16px; white-space: nowrap; }
</style>
</head>
<body>
  <section class="card card-front" aria-label="Business card front">
    <svg class="front-shape" viewBox="0 0 700 400" aria-hidden="true">
      <path d="M0,238 C230,230 500,190 700,8 L700,400 L0,400 Z" fill="var(--accent)"/>
      <path d="M0,246 C230,240 505,200 700,22 L700,400 L0,400 Z" fill="var(--card-black)"/>
    </svg>
    <div class="brand">
      <span class="brand-dot"></span>
      <span class="brand-name"><span class="line">Marrowby's</span><span class="line">Vacation Rentals</span></span>
    </div>
    <div class="contact">
      <div class="contact-head">
        <span class="person-name">Daniel Reyes</span>
        <span class="divider">|</span>
        <span class="person-title">CEO/Founder</span>
      </div>
      <div class="contact-row">
        <svg class="icon" viewBox="0 0 16 16" aria-hidden="true"><path d="M3 1h3l1.5 4-2 1.5a9 9 0 0 0 4 4L11 8.5l4 1.5v3a2 2 0 0 1-2 2A12 12 0 0 1 1 3a2 2 0 0 1 2-2z" fill="var(--accent)"/></svg>
        <span>555 210 4478</span>
        <span class="gap"></span>
        <svg class="icon" viewBox="0 0 16 16" aria-hidden="true"><rect x="1" y="3" width="14" height="10" rx="1" fill="var(--accent)"/><path d="M1.5 3.5 8 9l6.5-5.5" stroke="var(--card-black)" stroke-width="1.4" fill="none"/></svg>
        <span>info@mvrentals.com</span>
        <span class="gap"></span>
        <svg class="icon" viewBox="0 0 16 16" aria-hidden="true"><circle cx="8" cy="8" r="7" fill="var(--accent)"/><path d="M1 8h14M8 1c3 3 3 11 0 14M8 1c-3 3-3 11 0 14" stroke="var(--card-black)" stroke-width="1" fill="none"/></svg>
        <span>www.mvrentals.com</span>
      </div>
      <div class="contact-row">
        <svg class="icon" viewBox="0 0 16 16" aria-hidden="true"><path d="M8 1a5 5 0 0 1 5 5c0 4-5 9-5 9S3 10 3 6a5 5 0 0 1 5-5z" fill="var(--accent)"/><circle cx="8" cy="6" r="1.8" fill="var(--card-black)"/></svg>
        <span>4120 Coral Bay Road, Punta Cana, DR 23000</span>
      </div>
    </div>
  </section>

  <section class="card card-back" aria-label="Business card back">
    <div class="villa-photo" role="img" aria-label="Photograph of a white two-storey villa with arched balconies, palm trees and a blue pool with lounge chairs"></div>
    <div class="back-brand">
      <span class="brand-dot"></span>
      <span class="brand-name">Marrowby's Vacation Rentals</span>
    </div>
  </section>
</body>
</html>
```